Wedding Day Custom Wine Label - Tasmanian (Tamar Valley) wine

I am looking for a custom design that will be put on a wine label to commemorate a very good friend's wedding day.

We will need to be able to take the design and print it on to sticker labels that we can put on to wine bottles.

The bride and groom have asked for a simplistic label design (see example image attached). We need two labels. One for "Pinot Noir" wine and the other for "Chardonnay" wine. We would like the label to say:

The Hartwell's
Pinot Noir
2023
Tamar Valley

and for for the other wine variety:

The Hartwell's
Chardonnay
2023
Tamar Valley

smaller text below to say:

13.5% ALC/VOL 750ML
MEGAN & LIAM - 31.10.2024

I am happy to consider other variations - the bride & groom would prefer something minimalistic. Elegant and classy.

Target Market(s)

the bride & groom

Requirements
Must have
• Wedding date (31.10.2024). Wine type (Pinot Noir or Chardonnay).
Should not have
• images not essential

```html
<!DOCTYPE html>
<html lang="en">
<head>
<meta charset="UTF-8">
<title>The Hartwell's Wedding Wine Labels</title>
<link rel="stylesheet" href="https://fonts.googleapis.com/css2?family=Archivo:wdth,wght@125,300;125,400&display=swap">
<style>
  :root {
    --backdrop: #a59d90;
    --label-paper: #ffffff;
    --ink: #3a3a3a;
    --rule: #6a6a6a;
  }
  * { margin: 0; padding: 0; box-sizing: border-box; }
  html, body {
    width: 1200px;
    height: 1200px;
    overflow: hidden;
    background: var(--backdrop);
  }
  .canvas {
    position: relative;
    width: 1200px;
    height: 1200px;
    display: flex;
    justify-content: center;
    align-items: center;
    gap: 80px;
  }
  .wine-label {
    position: relative;
    width: 420px;
    height: 659px;
    background: var(--label-paper);
    color: var(--ink);
    font-family: "Archivo", "Helvetica Neue", Arial, sans-serif;
    font-stretch: 125%;
    font-weight: 300;
    line-height: 1;
  }
  .wine-label > * {
    position: absolute;
    left: 41px;
    white-space: nowrap;
  }
  .family-name {
    top: 68px;
    font-size: 27px;
    letter-spacing: 0.06em;
  }
  .variety, .region {
    font-size: 40px;
    letter-spacing: 0.08em;
  }
  .variety { top: 206px; }
  .region { top: 253px; }
  .vintage-row {
    top: 303px;
    right: 42px;
    display: flex;
    align-items: center;
    gap: 16px;
  }
  .vintage {
    font-size: 27px;
    letter-spacing: 0.22em;
  }
  .vintage-rule {
    flex: 1;
    height: 1px;
    background: var(--rule);
    margin-top: 8px;
  }
  .volume {
    top: 440px;
    font-size: 15px;
    letter-spacing: -0.02em;
  }
  .volume .small { font-size: 12px; }
  .wedding-date {
    top: 540px;
    font-size: 20px;
    letter-spacing: 0.12em;
  }
  .couple {
    top: 573px;
    font-size: 24px;
    letter-spacing: 0.3em;
  }
  .couple .amp {
    font-size: 13px;
    letter-spacing: 0.3em;
  }
</style>
</head>
<body>
  <main class="canvas">
    <article class="wine-label wine-label--pinot">
      <p class="family-name">THE HARTWELL'S</p>
      <h1 class="variety">PINOT NOIR</h1>
      <p class="region">TAMAR VALLEY</p>
      <div class="vintage-row">
        <span class="vintage">2023</span>
        <span class="vintage-rule"></span>
      </div>
      <p class="volume"><span class="small">13.5%</span> ALC/VOL <span class="small">750</span>ML</p>
      <p class="wedding-date">31.10.2024</p>
      <p class="couple">MEGAN <span class="amp">&amp;</span> LIAM</p>
    </article>

    <article class="wine-label wine-label--chardonnay">
      <p class="family-name">THE HARTWELL'S</p>
      <h1 class="variety">CHARDONNAY</h1>
      <p class="region">TAMAR VALLEY</p>
      <div class="vintage-row">
        <span class="vintage">2023</span>
        <span class="vintage-rule"></span>
      </div>
      <p class="volume"><span class="small">13.5%</span> ALC/VOL <span class="small">750</span>ML</p>
      <p class="wedding-date">31.10.2024</p>
      <p class="couple">MEGAN <span class="amp">&amp;</span> LIAM</p>
    </article>
  </main>
</body>
</html>
```